Gymnastics Award Design Needed--for kids

Need a gymnastics certificate or award designed. Will be printed on a piece of 8.5x11 paper. The award will be celebrating the gymnast learning a new skill in gymnastics. So it should be fun, but still look "official". Needs to look good hanging on a gymnast's bedroom wall.

It should say "The Aerial Cartwheel Club"
I will be using this design to change it based on the skill.

My main colors are:
#34475D
#E1467A
#7555A4

So should use those, but can add others

My website is tumblenest.net so you can see the look/feel.

Target Market(s)

Main audience will be girls ages 5-12, but will also be used by slightly older girls and boys. So needs to be fun, not too gender specific.

Industry/Entity Type

Learning

Requirements
Must have
• The following will need to go on the certificate:
• * Name of Skill
• * Image of Skill
• * Gymnast's Name
• * my logo
• * Gym's Logo
• * Gym's Name
• Optional: Date

```html
<!DOCTYPE html>
<html lang="en">
<head>
<meta charset="utf-8">
<title>The Aerial Cartwheel Club – Certificate</title>
<link rel="stylesheet" href="https://fonts.googleapis.com/css2?family=Quicksand:wght@400;500&family=Parisienne&display=swap">
<style>
  :root {
    --navy: #34475D;
    --pink: #E1467A;
    --purple: #7555A4;
    --violet: #8B5CF6;
    --ground: #C9CDD3;
    --paper: #FFFFFF;
    --badge: #111111;
  }
  html, body {
    margin: 0;
    padding: 0;
    overflow: hidden;
    background: var(--paper);
  }
  .certificate {
    position: relative;
    width: 1200px;
    height: 927px;
    background: var(--paper);
    font-family: "Quicksand", sans-serif;
    overflow: hidden;
  }
  .frame {
    position: absolute;
    inset: 0;
  }
  .title {
    position: absolute;
    top: 78px;
    left: 0;
    width: 100%;
    margin: 0;
    text-align: center;
    font-weight: 400;
    font-size: 76px;
    letter-spacing: 1px;
    color: var(--pink);
  }
  .skill-image {
    position: absolute;
    left: 319px;
    top: 226px;
    width: 547px;
    height: 144px;
    background: linear-gradient(90deg, #F2DCCB 0%, #3E3F8F 35%, #F2DCCB 60%, #3E3F8F 100%);
    opacity: 0.35;
  }
  .ground-line {
    position: absolute;
    left: 319px;
    top: 371px;
    width: 547px;
    height: 3px;
    background: var(--ground);
  }
  .skill-name {
    position: absolute;
    top: 388px;
    left: 0;
    width: 100%;
    margin: 0;
    text-align: center;
    font-weight: 400;
    font-size: 50px;
    color: var(--purple);
  }
  .gymnast-name {
    position: absolute;
    top: 530px;
    left: 0;
    width: 100%;
    margin: 0;
    text-align: center;
    font-family: "Parisienne", cursive;
    font-weight: 400;
    font-size: 112px;
    color: var(--navy);
  }
  .date-field {
    position: absolute;
    left: 76px;
    top: 770px;
    width: 314px;
    text-align: center;
    color: var(--navy);
  }
  .date-value {
    font-size: 44px;
    line-height: 50px;
    border-bottom: 2px solid var(--navy);
    padding-bottom: 2px;
  }
  .field-label {
    font-size: 32px;
    margin-top: 14px;
  }
  .partner-name {
    position: absolute;
    left: 436px;
    top: 770px;
    width: 320px;
    display: flex;
    align-items: center;
    gap: 12px;
    font-size: 36px;
    font-weight: 500;
    color: var(--violet);
  }
  .partner-dot {
    width: 34px;
    height: 34px;
    border-radius: 50%;
    background: var(--violet);
  }
  .gym-field {
    position: absolute;
    left: 846px;
    top: 690px;
    width: 240px;
    text-align: center;
    color: var(--navy);
  }
  .gym-badge {
    width: 120px;
    height: 120px;
    margin: 0 auto;
    border-radius: 50%;
    background: var(--badge);
  }
  .gym-title {
    font-size: 22px;
    font-weight: 500;
    margin-top: 8px;
    color: var(--navy);
  }
  .gym-field .field-label {
    margin-top: 4px;
  }
</style>
</head>
<body>
  <main class="certificate">
    <svg class="frame" width="1200" height="927" viewBox="0 0 1200 927" aria-hidden="true">
      <rect x="12" y="12" width="1176" height="903" rx="18" fill="none" stroke="#7555A4" stroke-width="2"/>
      <rect x="22" y="22" width="1156" height="883" rx="12" fill="none" stroke="#7555A4" stroke-width="1.5"/>
    </svg>

    <h1 class="title">The Aerial Cartwheel Club</h1>

    <div class="skill-image" role="img" aria-label="Illustration of a gymnast performing each stage of a front handspring"></div>
    <div class="ground-line"></div>
    <h2 class="skill-name">Front Handspring</h2>

    <p class="gymnast-name">First Last</p>

    <div class="date-field">
      <div class="date-value">MM/DD/YYY</div>
      <div class="field-label">Date</div>
    </div>

    <div class="partner-name">
      <span class="partner-dot"></span>
      <span>Tumble Nest</span>
    </div>

    <div class="gym-field">
      <div class="gym-badge"></div>
      <div class="gym-title">Summit Gymnastics</div>
      <div class="field-label">Gym Name</div>
    </div>
  </main>
</body>
</html>
```